Business Card

We need a business card for a fundraising/sales and marketing company called Brightwell Giving services. The logo colours are Red Black and white. The final design should communicate professional, reliable yet fun and charity minded
Updates

Sorry for the delay. A decision will be made in the next 48 hours. we are stuck between two designs. Kind Regards, Laura Dunmore

Industry/Entity Type

Marketing

```html
<!DOCTYPE html>
<html lang="en">
<head>
<meta charset="utf-8">
<title>Brightwell Giving – Business Card</title>
<link rel="stylesheet" href="https://fonts.googleapis.com/css2?family=Open+Sans:wght@400;600;700&display=swap">
<style>
  :root {
    --stage: #1c1c1c;
    --stage-edge: #0b0b0b;
    --card-black: #0d0d0d;
    --card-white: #ffffff;
    --brand-red: #d7261e;
    --swoosh-dark: #3f3d3d;
    --swoosh-light: #8a8888;
    --ink: #3a3a3a;
  }
  * { box-sizing: border-box; margin: 0; padding: 0; }
  html, body {
    width: 1200px; height: 944px; overflow: hidden;
    background: radial-gradient(ellipse at 50% 40%, var(--stage) 0%, var(--stage-edge) 80%);
    font-family: "Open Sans", Arial, sans-serif;
  }
  .canvas {
    position: relative; width: 1200px; height: 944px;
    display: flex; flex-direction: column; align-items: center; justify-content: center; gap: 64px;
  }
  .card {
    position: relative; width: 560px; height: 320px; overflow: hidden;
    box-shadow: 0 18px 40px rgba(0,0,0,.6);
  }
  /* Front */
  .card-front {
    background: linear-gradient(120deg, var(--card-black) 0%, #1e1e1e 48%, #2b2b2b 52%, var(--card-black) 100%);
    display: flex; align-items: center; justify-content: center;
  }
  .brand { display: flex; align-items: center; gap: 14px; }
  .brand-dot { width: 22px; height: 22px; border-radius: 50%; background: var(--brand-red); }
  .brand-name { font-weight: 600; font-size: 36px; color: #ffffff; letter-spacing: .5px; }
  /* Back */
  .card-back { background: var(--card-white); }
  .card-back .shapes { position: absolute; inset: 0; }
  .card-back .brand { position: absolute; left: 34px; top: 60px; gap: 10px; }
  .card-back .brand-dot { width: 16px; height: 16px; }
  .card-back .brand-name { font-size: 26px; color: var(--brand-red); }
  .contact { position: absolute; left: 34px; top: 150px; list-style: none; }
  .contact li {
    display: flex; align-items: center; gap: 10px;
    font-size: 13px; color: var(--ink); line-height: 22px;
  }
  .contact svg { width: 13px; height: 13px; fill: var(--brand-red); flex: none; }
  .person {
    position: absolute; right: 22px; top: 196px; text-align: right; color: #fff;
    white-space: nowrap; z-index: 1;
  }
  .person-name { font-weight: 700; font-size: 18px; line-height: 24px; }
  .person-role { font-size: 12px; line-height: 16px; }
</style>
</head>
<body>
<main class="canvas">
  <section class="card card-front" aria-label="Card front">
    <div class="brand">
      <span class="brand-dot"></span>
      <span class="brand-name">Brightwell Giving</span>
    </div>
  </section>

  <section class="card card-back" aria-label="Card back">
    <svg class="shapes" viewBox="0 0 560 320" preserveAspectRatio="none" aria-hidden="true">
      <path d="M560 4 C430 28 380 210 130 298 C370 232 420 40 560 16 Z" fill="var(--swoosh-light)" opacity=".75"/>
      <path d="M560 16 C440 40 400 220 175 306 C395 240 430 56 560 30 Z" fill="var(--swoosh-dark)"/>
      <path d="M560 30 C450 50 420 230 220 320 L560 320 Z" fill="var(--brand-red)"/>
      <path d="M0 296 C120 282 240 296 330 320 L0 320 Z" fill="var(--swoosh-dark)"/>
      <path d="M0 308 C110 298 200 308 260 320 L0 320 Z" fill="var(--brand-red)"/>
    </svg>

    <div class="brand">
      <span class="brand-dot"></span>
      <span class="brand-name">Brightwell Giving</span>
    </div>

    <ul class="contact">
      <li><svg viewBox="0 0 24 24"><path d="M12 2a7 7 0 0 0-7 7c0 5 7 13 7 13s7-8 7-13a7 7 0 0 0-7-7zm0 9.5A2.5 2.5 0 1 1 12 6a2.5 2.5 0 0 1 0 5.5z"/></svg>Your current or commercial address</li>
      <li><svg viewBox="0 0 24 24"><path d="M6.6 10.8a15 15 0 0 0 6.6 6.6l2.2-2.2a1 1 0 0 1 1-.25 11.4 11.4 0 0 0 3.6.57 1 1 0 0 1 1 1V20a1 1 0 0 1-1 1A17 17 0 0 1 3 4a1 1 0 0 1 1-1h3.5a1 1 0 0 1 1 1c0 1.25.2 2.45.57 3.57a1 1 0 0 1-.25 1z"/></svg>00.00.00.0000</li>
      <li><svg viewBox="0 0 24 24"><path d="M2 5h20v14H2zm2 2v.5l8 5 8-5V7l-8 5z"/></svg>yourname@yourwebsite.com</li>
      <li><svg viewBox="0 0 24 24"><path d="M12 2a10 10 0 1 0 0 20 10 10 0 0 0 0-20zm6.9 6h-3a15 15 0 0 0-1.3-3.9A8 8 0 0 1 18.9 8zM12 4c.8 1.2 1.5 2.5 1.9 4h-3.8c.4-1.5 1.1-2.8 1.9-4zM4.3 14a8 8 0 0 1 0-4h3.4a16 16 0 0 0 0 4zm.8 2h3a15 15 0 0 0 1.3 3.9A8 8 0 0 1 5.1 16zm3-8h-3a8 8 0 0 1 4.3-3.9A15 15 0 0 0 8.1 8zM12 20c-.8-1.2-1.5-2.5-1.9-4h3.8c-.4 1.5-1.1 2.8-1.9 4zm2.3-6H9.7a14 14 0 0 1 0-4h4.6a14 14 0 0 1 0 4zm.3 5.9a15 15 0 0 0 1.3-3.9h3a8 8 0 0 1-4.3 3.9zm1.7-5.9a16 16 0 0 0 0-4h3.4a8 8 0 0 1 0 4z"/></svg>www.yourwebsite.com</li>
    </ul>

    <div class="person">
      <p class="person-name">Your Long Name</p>
      <p class="person-role">Director</p>
    </div>
  </section>
</main>
</body>
</html>
```